This Project is listed for : Brisko only ... if you are not Briskos, please do not submit please

This is the listing for

Torvexa

business cards
very simple, elegant and firm
Black / Red / White

Target Market(s)

Adults
Investors
Clients

Industry/Entity Type

Business

Font styles to use
Decorative
Script

```html
<!DOCTYPE html>
<html lang="en">
<head>
<meta charset="utf-8">
<title>Torvexa business cards</title>
<link href="https://fonts.googleapis.com/css2?family=Courier+Prime:wght@400;700&display=swap" rel="stylesheet">
<style>
  :root {
    --backdrop: #2a2b2e;
    --paper: #e9e7e3;
    --ink: #2f2f31;
    --charcoal: #3d3d40;
    --charcoal-text: #c9c7c3;
    --accent-red: #b3302c;
  }
  * { margin: 0; padding: 0; box-sizing: border-box; }
  html, body { width: 1200px; height: 750px; overflow: hidden; }
  body {
    background: var(--backdrop);
    font-family: "Courier Prime", "Courier New", monospace;
    position: relative;
  }
  .card {
    position: absolute;
    left: 320px;
    width: 560px;
    height: 320px;
    overflow: hidden;
    background: var(--paper);
  }
  .card-front { top: 40px; }
  .card-back { top: 390px; }

  .front-rule {
    position: absolute;
    top: 50px;
    width: 3px;
    height: 90px;
    background: var(--accent-red);
  }
  .front-rule-left { left: 60px; top: 180px; }
  .front-rule-right { right: 60px; }

  .brand {
    position: absolute;
    display: flex;
    flex-direction: column;
    align-items: center;
    gap: 10px;
    transform: translate(-50%, -50%);
  }
  .card-front .brand { left: 50%; top: 50%; }
  .card-back .brand { left: 135px; top: 50%; }
  .brand-dot {
    width: 46px; height: 46px;
    border-radius: 50%;
    background: var(--ink);
  }
  .card-back .brand-dot { width: 38px; height: 38px; }
  .brand-name {
    font-weight: 700;
    font-size: 34px;
    color: var(--ink);
    letter-spacing: 1px;
  }
  .card-back .brand-name { font-size: 26px; }

  .info-panel {
    position: absolute;
    left: 270px; top: 0;
    width: 290px; height: 320px;
    background: var(--charcoal);
    border-left: 4px solid var(--accent-red);
    color: var(--charcoal-text);
    padding: 36px 30px 0 34px;
  }
  .person-name { font-size: 25px; letter-spacing: 1px; }
  .person-role { font-size: 13px; letter-spacing: 1.5px; margin-top: 4px; text-transform: uppercase; }
  .contact-list { list-style: none; margin-top: 60px; }
  .contact-item {
    display: flex; align-items: flex-start; gap: 12px;
    font-size: 14px; line-height: 18px; margin-bottom: 6px;
  }
  .contact-icon { width: 14px; height: 14px; flex: none; margin-top: 2px; }
</style>
</head>
<body>
  <section class="card card-front">
    <span class="front-rule front-rule-left"></span>
    <span class="front-rule front-rule-right"></span>
    <div class="brand">
      <span class="brand-dot"></span>
      <span class="brand-name">Torvexa</span>
    </div>
  </section>

  <section class="card card-back">
    <div class="brand">
      <span class="brand-dot"></span>
      <span class="brand-name">Torvexa</span>
    </div>
    <div class="info-panel">
      <p class="person-name">Marcus Hale</p>
      <p class="person-role">CEO and founder</p>
      <ul class="contact-list">
        <li class="contact-item">
          <svg class="contact-icon" viewBox="0 0 14 14"><rect x="3" y="0.5" width="8" height="13" rx="1.5" fill="none" stroke="currentColor" stroke-width="1.4"/><circle cx="7" cy="11" r="0.9" fill="currentColor"/></svg>
          <span>+1 555 204 718 6</span>
        </li>
        <li class="contact-item">
          <svg class="contact-icon" viewBox="0 0 14 14"><path d="M3 1 L5.5 1 L6.5 4 L5 5.2 Q6.5 8.5 8.8 9 L10 7.5 L13 8.5 L13 11 Q13 13 10.5 13 Q1 12 1 3.5 Q1 1 3 1 Z" fill="currentColor"/></svg>
          <span>+1 555 204 718 6</span>
        </li>
        <li class="contact-item">
          <svg class="contact-icon" viewBox="0 0 14 14"><rect x="0.7" y="2.5" width="12.6" height="9" fill="none" stroke="currentColor" stroke-width="1.4"/><path d="M1 3 L7 8 L13 3" fill="none" stroke="currentColor" stroke-width="1.4"/></svg>
          <span>contact@torvexa.com</span>
        </li>
        <li class="contact-item">
          <svg class="contact-icon" viewBox="0 0 14 14"><path d="M7 13.5 Q2 7.5 2 5 A5 5 0 0 1 12 5 Q12 7.5 7 13.5 Z" fill="currentColor"/><circle cx="7" cy="5" r="1.8" fill="var(--charcoal)"/></svg>
          <span>street example<br>number 34 town</span>
        </li>
      </ul>
    </div>
  </section>
</body>
</html>
```